QTM Website revamping

Make a website main page, navigation / menu options, couple of product pages in the 4 product categories, improvement on About us.
Our Website will need to be in PHP.
Our competitors websites for an idea.
www.norvask.com
https://frost.halbrook.com/en-gb/brands/tovrin
www.lumba.it
www.sarni.it
Our website is temporarily hosted at https://www.brightmarkweb.com/qtm/
Once done, we would like a quote for coding the entire website as well. If we find the quote good we will go ahead with you.

Target Market(s)

Industrial and Commercial Refrigeration , Cold Store, freezer and chiller manufacturers and commercial Airconditioning contractors and Industrial Automation panel makers.

Industry/Entity Type

Engineering

Number of Pages Required

5+ page

Font styles to use
Other font styles liked:
• "Michroma" "Roboto" "MONTSERRAT"

Colors
3377b5
ffffff

Requirements
Must have
• Main page, index/menu, couple of product pages.
Nice to have
• A good navigation to the product list
Font should be similar to the top menu line
Showcase our site as a good electronics temperature controller manufacturer for Refrigeration / Industrial Process Automation

```html
<!DOCTYPE html>
<html lang="en">
<head>
<meta charset="utf-8">
<title>QTM Controls – Refrigeration &amp; Automation Controllers</title>
<link rel="stylesheet" href="https://fonts.googleapis.com/css2?family=Montserrat:wght@400;500;600;700;800;900&display=swap">
<style>
:root{
  --blue:#3377b5;
  --blue-dark:#25609a;
  --red:#e3373b;
  --ink:#222;
  --heading:#444;
  --muted:#777;
  --light:#f2f2f2;
  --white:#fff;
  --black:#000;
}
*{box-sizing:border-box;margin:0;padding:0}
html,body{width:1200px;height:2583px;overflow:hidden;background:var(--white)}
body{font-family:'Montserrat',sans-serif;color:var(--ink);position:relative}
.abs{position:absolute}
a{color:inherit;text-decoration:none}

/* header */
.top-rule{left:208px;top:0;width:780px;height:4px;background:var(--red)}
.brand{left:208px;top:18px;width:46px;height:28px;border:2px solid var(--red);display:flex;align-items:center;justify-content:center;font-weight:800;font-size:13px;color:var(--red);letter-spacing:1px;background:var(--white)}
.contact-top{top:26px;font-size:10px;color:var(--blue);display:flex;align-items:center;gap:6px;white-space:nowrap}
.nav{left:208px;top:60px;width:780px;height:37px;background:var(--black);z-index:3}
.nav-item{font-size:9px;font-weight:700;color:var(--white);letter-spacing:.3px;display:flex;align-items:center;gap:4px;white-space:nowrap}
.nav-item svg{width:7px;height:5px}
.search{left:734px;top:69px;width:246px;height:20px;border:1px solid #444;background:var(--black)}
.search-btn{left:963px;top:71px;width:15px;height:15px;background:var(--red);border-radius:2px;display:flex;align-items:center;justify-content:center}

/* hero */
.hero{left:0;top:77px;width:1200px;height:548px;background:radial-gradient(ellipse at 25% 55%,#8ea6d2 0%,#4f6fab 35%,#2d4f8e 70%,#233f78 100%)}
.hero-title{left:0;width:1200px;text-align:center;color:var(--white);white-space:nowrap}
.h-main{top:184px;font-size:46px;font-weight:900;letter-spacing:1px}
.h-sub{top:235px;font-size:29px;font-weight:500;letter-spacing:.5px}
.h-mark{left:415px;top:270px;width:366px;height:38px;background:#4b8fd6;color:var(--white);font-size:31px;font-weight:900;text-align:center;line-height:38px;letter-spacing:.5px;white-space:nowrap}
.btn-outline{left:523px;top:336px;width:151px;height:32px;border:1px solid var(--white);border-radius:16px;color:var(--white);font-size:11px;font-weight:600;display:flex;align-items:center;justify-content:center;gap:6px;white-space:nowrap}
.hero-arrow{top:355px}

/* about */
.about-photo{left:208px;top:487px;width:372px;height:296px;background:linear-gradient(135deg,#e9e9e9 0%,#c9c9c9 50%,#7d7d7d 100%);z-index:2}
.about-frame{left:259px;top:532px;width:341px;height:271px;border:3px solid var(--blue);z-index:2}
.welcome{left:641px;top:558px;color:var(--white);font-size:15px;font-weight:600}
.welcome-name{left:641px;top:570px;color:var(--white);font-size:29px;font-weight:700;white-space:nowrap}
.about-copy{left:641px;top:648px;width:346px;font-size:9px;line-height:14px;color:#444}
.btn-blue{background:var(--blue);color:var(--white);border-radius:17px;font-weight:600;display:flex;align-items:center;justify-content:center;gap:5px;white-space:nowrap}

/* section heads */
.sec-title{left:0;width:1200px;text-align:center;font-size:23px;font-weight:600;color:var(--heading)}
.sec-bar{width:43px;height:4px;background:#d0d0d0;border-radius:2px}
.sec-sub{left:0;width:1200px;text-align:center;font-size:10.5px;color:var(--muted);letter-spacing:.6px}

/* categories */
.cat-img{top:982px;width:183px;height:132px}
.cat-label{top:1100px;width:162px;height:31px;background:var(--blue);color:var(--white);font-size:11px;font-weight:700;border-radius:3px;display:flex;align-items:center;justify-content:center;white-space:nowrap}

/* highlights */
.band{left:0;top:1193px;width:1200px;height:524px;background:var(--light)}
.card{top:1352px;width:181px;height:236px;background:var(--white)}
.card-img{position:absolute;left:20px;top:14px;width:141px;height:122px;border-radius:6px}
.card-name{position:absolute;left:22px;top:166px;width:145px;font-size:11px;font-weight:700;color:#333;line-height:14px}
.card-link{position:absolute;left:22px;top:205px;font-size:10px;color:var(--muted);display:flex;align-items:center;gap:5px}

/* events / clients */
.clients-bg{left:598px;top:1717px;width:602px;height:578px;background:var(--light)}
.split-title{font-size:22px;font-weight:600;color:#666;white-space:nowrap}
.split-title span{color:var(--blue)}
.timeline{left:214px;top:1888px;width:2px;height:316px;background:var(--red)}
.tl-dot{width:12px;height:12px;border-radius:50%;background:var(--red);left:209px}
.date-tag{left:232px;height:23px;background:var(--red);color:var(--white);font-size:9px;font-weight:700;display:flex;align-items:center;padding:0 8px;white-space:nowrap}
.venue{left:233px;font-size:9.5px;color:#444;line-height:12px;white-space:nowrap}
.expo-box{left:418px;width:138px;height:59px;background:#ededed;display:flex;align-items:center;justify-content:center;font-size:14px;font-weight:700;color:var(--blue);white-space:nowrap}
.client{width:125px;text-align:center;font-size:12px;font-weight:700;color:var(--blue);white-space:nowrap}

/* footer */
.foot-rule{left:0;top:2295px;width:1200px;height:2px;background:var(--red)}
.social{top:2416px;width:18px;height:18px;border-radius:50%;background:var(--black)}
.foot-links{font-size:9.5px;color:#333;line-height:19px;list-style:none}
.foot-addr{left:783px;top:2363px;font-size:9.5px;color:#333;line-height:19px;white-space:nowrap}
.foot-phone{left:786px;top:2436px;font-size:13px;font-weight:600;color:#222}
.foot-mail{left:786px;top:2458px;font-size:10px;font-weight:600;color:#222}
.copy{left:208px;top:2540px;font-size:8.5px;color:#333}
</style>
</head>
<body>

<!-- header -->
<div class="abs top-rule"></div>
<div class="abs brand">QTM</div>
<div class="abs contact-top" style="left:733px">
  <svg width="14" height="14" viewBox="0 0 14 14"><circle cx="7" cy="7" r="6.2" fill="none" stroke="#222" stroke-width="1"/><path d="M4.6 4.2l1.3-.4.8 1.7-.8.6q.7 1.5 2.1 2.1l.6-.8 1.7.8-.4 1.3q-3.9-.6-5.3-5.3z" fill="#222"/></svg>
  +91-22-40615500
</div>
<div class="abs contact-top" style="left:855px">
  <svg width="15" height="11" viewBox="0 0 15 11"><rect x=".6" y=".6" width="13.8" height="9.8" rx="1" fill="none" stroke="#222"/><path d="M1 1.2l6.5 5 6.5-5" fill="none" stroke="#222"/></svg>
  sales@qtmcontrols.com
</div>

<nav class="abs nav"></nav>
<div class="abs nav-item" style="left:232px;top:74px;z-index:4">PRODUCTS <svg viewBox="0 0 7 5"><path d="M.5 .8l3 3 3-3" fill="none" stroke="#e3373b" stroke-width="1.4"/></svg></div>
<div class="abs nav-item" style="left:317px;top:74px;z-index:4">ABOUT US</div>
<div class="abs nav-item" style="left:398px;top:74px;z-index:4">RESOURCES <svg viewBox="0 0 7 5"><path d="M.5 .8l3 3 3-3" fill="none" stroke="#e3373b" stroke-width="1.4"/></svg></div>
<div class="abs nav-item" style="left:489px;top:74px;z-index:4">HIGHLIGHTS <svg viewBox="0 0 7 5"><path d="M.5 .8l3 3 3-3" fill="none" stroke="#e3373b" stroke-width="1.4"/></svg></div>
<div class="abs nav-item" style="left:579px;top:74px;z-index:4">CONTACT</div>
<div class="abs search" style="z-index:4"></div>
<div class="abs search-btn" style="z-index:5"><svg width="9" height="9" viewBox="0 0 9 9"><circle cx="3.6" cy="3.6" r="2.6" fill="none" stroke="#fff" stroke-width="1.2"/><path d="M5.5 5.5L8.3 8.3" stroke="#fff" stroke-width="1.4"/></svg></div>

<!-- hero -->
<section class="abs hero" role="img" aria-label="Close-up of frosted berries in cool blue light"></section>
<div class="abs hero-title h-main">REFRIGERATION</div>
<div class="abs hero-title h-sub">SUPPLYING INDIA WITH ADVANCED</div>
<div class="abs h-mark">COOLING SOLUTIONS</div>
<a class="abs btn-outline">Explore All Products
  <svg width="9" height="8" viewBox="0 0 9 8"><path d="M1 1l3 3-3 3M5 1l3 3-3 3" fill="none" stroke="#fff" stroke-width="1.4"/></svg></a>
<svg class="abs hero-arrow" style="left:121px" width="26" height="18" viewBox="0 0 26 18"><path d="M9 2L2 9l7 7" fill="none" stroke="#fff" stroke-width="2"/><path d="M4 9h4M11 9h3M17 9h3M22 9h3" stroke="#fff" stroke-width="2.5"/></svg>
<svg class="abs hero-arrow" style="left:1040px" width="26" height="18" viewBox="0 0 26 18"><path d="M17 2l7 7-7 7" fill="none" stroke="#fff" stroke-width="2"/><path d="M1 9h3M6 9h3M12 9h3M18 9h4" stroke="#fff" stroke-width="2.5"/></svg>

<!-- about -->
<div class="abs about-photo" role="img" aria-label="Technician operating a cold-storage production machine in a clean factory hall"></div>
<div class="abs about-frame"></div>
<div class="abs welcome">Welcome to</div>
<h1 class="abs welcome-name">QTM Controls</h1>
<p class="abs about-copy">The evolution of B.K. Controls Pvt Ltd into QTM Controls has helped to leverage the strengths of our design team and to expand our product portfolio. Our recent focus on the need for Automation has resulted in the launch of a highly customizable and user-friendly range of PLC's, HMI's and related products. We are very excited to showcase this technology as part of our Frostline range.</p>
<a class="abs btn-blue" style="left:641px;top:741px;width:100px;height:33px;font-size:9.5px">More About Us
  <svg width="6" height="9" viewBox="0 0 6 9"><path d="M1 1l3.5 3.5L1 8" fill="none" stroke="#fff" stroke-width="1.6"/></svg></a>

<!-- product categories -->
<h2 class="abs sec-title" style="top:877px">Product Categories</h2>
<div class="abs sec-sub" style="top:913px">THE WIDEST RANGE OF HVAC&amp;R AND PROCESS CONTROL INSTRUMENTATION.</div>
<div class="abs sec-bar" style="left:578px;top:940px"></div>

<div class="abs cat-img" style="left:208px;background:linear-gradient(135deg,#c9cdd2,#d8686c 55%,#8a8f93)" role="img" aria-label="Raspberries and mint on ice"></div>
<div class="abs cat-img" style="left:407px;background:linear-gradient(135deg,#d4d6d8,#aeb1b4 60%,#8b8e91)" role="img" aria-label="Electrical control panels with switches"></div>
<div class="abs cat-img" style="left:606px;background:linear-gradient(135deg,#c9d8ec,#9db7d8 55%,#5d7897)" role="img" aria-label="Robotic arm in an automated plant"></div>
<div class="abs cat-img" style="left:805px;background:linear-gradient(135deg,#7e8790,#3f4851 55%,#1e252c)" role="img" aria-label="Industrial pipework and valves"></div>
<div class="abs cat-label" style="left:219px">HVAC&amp;R Controllers</div>
<div class="abs cat-label" style="left:418px">HVACR Electrical Panels</div>
<div class="abs cat-label" style="left:617px">Industrial Automation</div>
<div class="abs cat-label" style="left:816px">Valves &amp; Controls</div>

<!-- product highlights -->
<section class="abs band"></section>
<h2 class="abs sec-title" style="top:1270px">Product Highlights</h2>
<div class="abs sec-bar" style="left:578px;top:1310px"></div>
<svg class="abs" style="left:164px;top:1464px" width="16" height="26" viewBox="0 0 16 26"><path d="M13 2L3 13l10 11" fill="none" stroke="#555" stroke-width="2"/></svg>
<svg class="abs" style="left:1015px;top:1464px" width="16" height="26" viewBox="0 0 16 26"><path d="M3 2l10 11L3 24" fill="none" stroke="#222" stroke-width="2"/></svg>

<article class="abs card" style="left:208px">
  <div class="card-img" style="background:linear-gradient(160deg,#fff 10%,#4a4a4a 45%,#222 70%,#fff 90%)" role="img" aria-label="Panel-mount relay controller with red digital display"></div>
  <div class="card-name">8A RELAY QR-4410T</div>
  <a class="card-link">Details <svg width="9" height="8" viewBox="0 0 9 8"><path d="M1 1l3 3-3 3M5 1l3 3-3 3" fill="none" stroke="#e3373b" stroke-width="1.5"/></svg></a>
</article>
<article class="abs card" style="left:408px">
  <div class="card-img" style="background:linear-gradient(90deg,#fff 5%,#1e1e1e 25%,#2a2a2a 50%,#eee 60%,#fff 95%)" role="img" aria-label="HACCP controller unit with multi-digit display"></div>
  <div class="card-name">HACCP HX-309100</div>
  <a class="card-link">Details <svg width="9" height="8" viewBox="0 0 9 8"><path d="M1 1l3 3-3 3M5 1l3 3-3 3" fill="none" stroke="#e3373b" stroke-width="1.5"/></svg></a>
</article>
<article class="abs card" style="left:608px">
  <div class="card-img" style="background:radial-gradient(circle at 50% 50%,#2e2e2e 35%,#8d8d8d 55%,#fff 70%)" role="img" aria-label="Square single-line display controller"></div>
  <div class="card-name">SINGLE LINE DISPLAY LD-150T</div>
  <a class="card-link">Details <svg width="9" height="8" viewBox="0 0 9 8"><path d="M1 1l3 3-3 3M5 1l3 3-3 3" fill="none" stroke="#e3373b" stroke-width="1.5"/></svg></a>
</article>
<article class="abs card" style="left:808px">
  <div class="card-img" style="background:radial-gradient(ellipse at 50% 55%,#e4e8f2 20%,#9aa6d0 38%,#fff 60%)" role="img" aria-label="White humidifier with angled outlet"></div>
  <div class="card-name">HUMIDIFIER</div>
  <a class="card-link">Details <svg width="9" height="8" viewBox="0 0 9 8"><path d="M1 1l3 3-3 3M5 1l3 3-3 3" fill="none" stroke="#e3373b" stroke-width="1.5"/></svg></a>
</article>
<a class="abs btn-blue" style="left:538px;top:1638px;width:121px;height:31px;font-size:10.5px">View All Products</a>

<!-- events -->
<div class="abs clients-bg"></div>
<h2 class="abs split-title" style="left:212px;top:1800px">Upcoming <span>Events</span></h2>
<div class="abs sec-bar" style="left:212px;top:1839px"></div>
<div class="abs timeline"></div>
<div class="abs" style="left:214px;top:1888px;width:14px;height:2px;background:var(--red)"></div>
<div class="abs" style="left:214px;top:2202px;width:18px;height:2px;background:var(--red)"></div>
<div class="abs" style="left:232px;top:1882px;display:flex;align-items:center;gap:5px;font-size:10px;font-weight:600;color:#333">
  <svg width="14" height="14" viewBox="0 0 14 14"><rect x=".6" y="1.6" width="12.8" height="11.8" fill="none" stroke="#333"/><path d="M.6 4.5h12.8M3 0v3M11 0v3" stroke="#333"/><path d="M3 7h1.5M6.3 7h1.5M9.6 7h1.5M3 10h1.5M6.3 10h1.5M9.6 10h1.5" stroke="#333" stroke-width="1.2"/></svg>
  Calendar
</div>

<div class="abs tl-dot" style="top:1916px"></div>
<div class="abs date-tag" style="top:1912px">29th to 31st October 2020</div>
<div class="abs venue" style="top:1944px">NORTHGATE EXPO CENTRE &amp; MART,<br>NEW DELHI, INDIA</div>
<div class="abs expo-box" style="top:1908px">Coolex Asia</div>

<div class="abs tl-dot" style="top:2009px"></div>
<div class="abs date-tag" style="top:2004px">25th to 27th February 2021</div>
<div class="abs venue" style="top:2036px">SOUTHFIELD INTERNATIONAL<br>EXHIBITION CENTRE, BENGALURU</div>
<div class="abs expo-box" style="top:2001px">Thermex 2021</div>

<div class="abs tl-dot" style="top:2101px"></div>
<div class="abs date-tag" style="top:2095px">22nd to 25th September 2021</div>
<div class="abs venue" style="top:2127px">HARBOUR EXPO HALL MUMBAI<br>Visit us at : Stall No. I-20 to I-23</div>
<div class="abs expo-box" style="top:2092px">Procon Expo 2021</div>

<a class="abs" style="left:251px;top:2196px;font-size:10px;font-weight:600;color:#333">View All</a>

<!-- clients -->
<h2 class="abs split-title" style="left:655px;top:1800px">Our <span>Clients</span></h2>
<div class="abs sec-bar" style="left:655px;top:1839px"></div>
<div class="abs client" style="left:633px;top:1907px">Petrovia</div>
<div class="abs client" style="left:759px;top:1907px">Coolmark</div>
<div class="abs client" style="left:885px;top:1907px">Astrel</div>
<div class="abs client" style="left:633px;top:1988px">Medora Pharma</div>
<div class="abs client" style="left:759px;top:1988px">Skyport Authority</div>
<div class="abs client" style="left:885px;top:1988px">Airvanta</div>
<div class="abs client" style="left:633px;top:2077px">Lumen</div>
<div class="abs client" style="left:759px;top:2077px">Kaizo</div>
<div class="abs client" style="left:885px;top:2077px">Railnet</div>
<div class="abs" style="left:815px;top:2150px;width:10px;height:10px;border-radius:50%;background:var(--blue)"></div>
<div class="abs" style="left:831px;top:2150px;width:10px;height:10px;border-radius:50%;background:#ccc"></div>

<!-- footer -->
<div class="abs foot-rule"></div>
<div class="abs brand" style="top:2369px">QTM</div>
<a class="abs social" style="left:208px" aria-label="Facebook"></a>
<a class="abs social" style="left:237px" aria-label="LinkedIn"></a>
<a class="abs social" style="left:265px" aria-label="Instagram"></a>
<a class="abs social" style="left:293px" aria-label="YouTube"></a>

<ul class="abs foot-links" style="left:491px;top:2361px">
  <li>Product Catalog</li><li>Software</li><li>Videos</li><li>Channel Network</li><li>Clientele</li><li>Expo and Events</li><li>Gallery</li>
</ul>
<ul class="abs foot-links" style="left:658px;top:2361px">
  <li>About Us</li><li>Products</li><li>Career</li><li>Contact</li><li>Sitemap</li>
</ul>
<address class="abs foot-addr" style="font-style:normal">B-42, Orion Industrial Park,<br>Sector 7, Kalwa Link Road,<br>Navi Mumbai – 400 712, INDIA.</address>
<div class="abs foot-phone">+91-22-40615500</div>
<div class="abs foot-mail">sales@qtmcontrols.com</div>

<div class="abs" style="left:793px;top:2512px;font-size:12px;font-weight:700;color:#333">Frostline</div>
<div class="abs" style="left:856px;top:2512px;font-size:12px;font-weight:700;color:#333">Keepwell</div>
<div class="abs" style="left:936px;top:2497px;width:52px;height:52px;border-radius:50%;background:var(--red)" role="img" aria-label="Made in country badge"></div>

<div class="abs copy">© 2020. All Rights Reserved.</div>

</body>
</html>
```